Book cover design for the book titled "Beneath the Undertow."

create a book cover. The book title is, "Beneath the Undertow: Why Early Wounds Keep Sinking Our Kind." The purpose of the book is to create awareness of how childhood trauma is impacting 7 out of 10 adults in the world today and that two-thirds of children will experience neglect and or abuse before their 18th birthday. One victim described that his mental and physical illness resulting from childhood trauma felt like he wa being pulled to the ground, that the force was "beneath the undertow." The design should be clean and simple and communicate a crisis.

```html
<!DOCTYPE html>
<html lang="en">
<head>
<meta charset="utf-8">
<title>Beneath the Undertow – Book Cover</title>
<link rel="stylesheet" href="https://fonts.googleapis.com/css2?family=Montserrat:wght@600;700&display=swap">
<style>
  :root {
    --page: #ffffff;
    --cover-ink: #121317;
    --title-orange: #fbae40;
    --text-white: #ffffff;
    --rule-grey: #9a9ca3;
    --deck-shadow: #0d0f13;
    --deck-dark: #2c3440;
    --deck-mid: #556170;
    --deck-light: #8e9aa9;
  }
  * { margin: 0; padding: 0; box-sizing: border-box; }
  html, body {
    width: 1200px;
    height: 1200px;
    overflow: hidden;
    background: var(--page);
  }
  .canvas {
    position: relative;
    width: 1200px;
    height: 1200px;
    background: var(--page);
  }
  .book-cover {
    position: absolute;
    left: 293px;
    top: 140px;
    width: 614px;
    height: 920px;
    background: var(--cover-ink);
    overflow: hidden;
    font-family: "Montserrat", sans-serif;
  }
  .cover-photo {
    position: absolute;
    left: 0;
    right: 0;
    top: 330px;
    bottom: 0;
    background:
      linear-gradient(180deg, var(--cover-ink) 0%, rgba(18,19,23,0.85) 8%, rgba(18,19,23,0) 26%),
      radial-gradient(ellipse 26% 34% at 56% 56%, rgba(8,9,12,0.95) 0%, rgba(8,9,12,0.8) 55%, rgba(8,9,12,0) 100%),
      radial-gradient(ellipse 70% 60% at 55% 50%, rgba(142,154,169,0) 40%, rgba(13,15,19,0.55) 100%),
      linear-gradient(160deg, var(--deck-dark) 0%, var(--deck-light) 35%, var(--deck-mid) 65%, var(--deck-dark) 100%);
  }
  .title-word {
    position: absolute;
    left: 0;
    right: 0;
    text-align: center;
    color: var(--title-orange);
    font-weight: 700;
    font-size: 92px;
    line-height: 1;
    letter-spacing: -0.02em;
  }
  .title-word--first { top: 30px; }
  .title-word--second { top: 158px; }
  .title-joiner {
    position: absolute;
    left: 42px;
    right: 42px;
    top: 131px;
    display: flex;
    align-items: center;
    gap: 10px;
    color: var(--text-white);
    font-weight: 700;
    font-size: 32px;
    line-height: 1;
  }
  .title-joiner::before,
  .title-joiner::after {
    content: "";
    flex: 1;
    height: 1px;
    background: var(--rule-grey);
  }
  .subtitle {
    position: absolute;
    left: 0;
    right: 0;
    top: 266px;
    text-align: center;
    color: var(--text-white);
    font-weight: 700;
    font-size: 34px;
    line-height: 40px;
  }
  .author-name {
    position: absolute;
    left: 0;
    right: 0;
    top: 753px;
    text-align: center;
    color: var(--text-white);
    font-weight: 700;
    font-size: 30px;
    line-height: 1;
    letter-spacing: 0.2em;
    padding-left: 0.2em;
  }
</style>
</head>
<body>
  <div class="canvas">
    <div class="book-cover">
      <div class="cover-photo" role="img" aria-label="Photograph seen from above of a small child in a dark jacket sitting alone on grey wooden decking with a few fallen leaves"></div>
      <h1 class="book-title">
        <span class="title-word title-word--first">BENEATH</span>
        <span class="title-joiner">THE</span>
        <span class="title-word title-word--second">UNDERTOW</span>
      </h1>
      <p class="subtitle">WHY EARLY WOUNDS KEEP<br>SINKING OUR KIND</p>
      <p class="author-name">AUTHOR NAME</p>
    </div>
  </div>
</body>
</html>
```